Quillbrook Health needs a new services brochure

We need a new brochure that highlights the services that we offer at our clinic. We are a multidisciplinary health clinic that focuses on injury rehabilitation and pain management. We are looking for a brochure that will highlight our primary services to our clientele and inform potential clients of what we can offer. We pride ourselves on our quality of care and our advanced treatment techniques.
Target Market(s)
young families, athletes, people interested in their health.
Industry/Entity Type
Health And Wellness
Colors
Designer to choose colors to be used in the design.
Requirements
Must have
- We would love our new brochure to be a tri-fold that has 6 pages. We would like it to have brief information about our featured services:
- - Chiropractic
- - Massage Therapy
- - Manual Osteopathic Therapy
- - Acupuncture
- - Laser Therapy
- - Radial Shockwave Therapy
- We would also like this brochure to include a brief price list and direct billing info, About Us section & Contact information.
Nice to have
- If there is space to list that we also offer other services such as : Tissue Unwind Method, Hot Stone Massage, Cupping Technique, Pembrill Method, and Kinesiology Taping that would be great. We would like to use images similar to those that are on our website (we have hi-res of all images on the website) www.quillbrookhealth.ca and colours that would fit with our logo.

```html
<!DOCTYPE html>
<html lang="en">
<head>
<meta charset="utf-8">
<title>Quillbrook Health – Services Brochure</title>
<link rel="stylesheet" href="https://fonts.googleapis.com/css2?family=Montserrat:wght@300;400;600;700;800&family=Open+Sans:wght@400;600&display=swap">
<style>
  :root{
    --canvas:#3b3b3d;
    --paper:#f4f5f7;
    --ink:#3a3d42;
    --blue:#1769b5;
    --blue-deep:#0b3f86;
    --blue-bright:#1f7fd0;
    --band-dark:#2b2c2f;
    --band-mid:#55585d;
    --pill:#2f3033;
    --white:#ffffff;
  }
  *{box-sizing:border-box;margin:0;padding:0}
  html,body{width:1200px;height:800px;overflow:hidden;background:var(--canvas)}
  body{font-family:"Open Sans",Arial,sans-serif;color:var(--ink)}

  .brochure{
    position:absolute;left:20px;top:20px;width:1160px;height:760px;
    display:grid;grid-template-columns:387px 387px 386px;
    box-shadow:0 18px 40px rgba(0,0,0,.45);
  }
  .panel{position:relative;height:760px;overflow:hidden}
  .panel--light{background:var(--paper);border-bottom:7px solid var(--blue)}
  .panel--light + .panel--light{border-left:1px solid #e2e4e8}

  .services-band{
    position:absolute;left:0;top:0;width:774px;height:62px;z-index:2;
    background:linear-gradient(90deg,var(--band-mid) 0%,var(--band-dark) 45%,var(--band-dark) 100%);
    display:flex;align-items:center;justify-content:center;
    font-family:"Montserrat",Arial,sans-serif;font-size:30px;color:var(--white);
    letter-spacing:26px;text-transform:uppercase;padding-left:26px;
  }
  .services-band .light{font-weight:300;margin-right:26px}
  .services-band .bold{font-weight:800}

  .panel-body{position:absolute;left:0;right:0;top:62px;bottom:0;padding:20px 26px 0}

  .service{display:grid;column-gap:16px;margin-bottom:18px;align-items:start}
  .service--img-right{grid-template-columns:1fr 122px}
  .service--img-left{grid-template-columns:122px 1fr}
  .service-title{
    font-family:"Montserrat",Arial,sans-serif;font-weight:700;font-size:16px;
    color:var(--blue);line-height:1.2;
  }
  .service-title::after{
    content:"";display:block;width:22px;height:3px;background:var(--ink);margin:6px 0 7px;
  }
  .service-text{font-size:10px;line-height:1.48;color:var(--ink);text-align:justify;hyphens:auto}

  .photo{position:relative;width:114px;height:96px;margin:0 8px 8px 0}
  .photo::after{
    content:"";position:absolute;left:12px;top:14px;right:-8px;bottom:-8px;
    border-right:2px solid var(--blue);border-bottom:2px solid var(--blue);
  }
  .photo-fill{position:absolute;inset:0;border-radius:1px}
  .photo--tall{height:140px}
  .photo--short{height:68px}

  .tone-skin{background:linear-gradient(135deg,#d9c2b1,#b28a73 55%,#5a4a44)}
  .tone-linen{background:linear-gradient(135deg,#f1eeea,#c8a48c 60%,#8e6c5b)}
  .tone-needle{background:linear-gradient(135deg,#3a2a24,#b67e60 50%,#e0b59a)}
  .tone-laser{background:linear-gradient(135deg,#cfd3da,#8c7f74 50%,#3f4652)}
  .tone-device-blue{background:linear-gradient(135deg,#0a2f7a,#2e7fe0 55%,#a9d2ff)}
  .tone-device-grey{background:linear-gradient(135deg,#f2f3f5,#c7cbd1 60%,#8f959d)}

  .stack{display:flex;flex-direction:column;gap:12px}

  .book{
    position:absolute;left:26px;right:26px;bottom:52px;
    height:38px;border-radius:19px;background:var(--pill);
    display:flex;align-items:center;justify-content:center;
    font-family:"Montserrat",Arial,sans-serif;font-weight:800;font-size:16px;
    color:var(--white);letter-spacing:1px;text-transform:uppercase;
  }
  .site{
    position:absolute;left:0;right:0;bottom:20px;
    display:flex;align-items:center;justify-content:center;gap:8px;
    font-family:"Montserrat",Arial,sans-serif;font-size:14px;color:var(--ink);
  }
  .site strong{color:var(--blue);font-weight:700}

  .panel--prices{
    background:linear-gradient(160deg,var(--blue-deep) 0%,var(--blue) 55%,var(--blue-bright) 100%);
    color:var(--white);padding:40px 30px 0 34px;
  }
  .prices-title{font-family:"Montserrat",Arial,sans-serif;font-size:24px;text-transform:uppercase;letter-spacing:1px}
  .prices-title .light{font-weight:300}
  .prices-title .bold{font-weight:800}
  .prices-title::after{content:"";display:block;width:26px;height:3px;background:var(--white);margin:8px 0 18px}

  .price-group{position:relative;padding-left:14px;margin-bottom:18px}
  .price-group::before{content:"";position:absolute;left:0;top:4px;bottom:2px;width:4px;background:rgba(0,0,0,.22);border-radius:2px}
  .price-group h3{font-family:"Montserrat",Arial,sans-serif;font-weight:700;font-size:15px;margin-bottom:5px}
  .price-row{display:grid;grid-template-columns:1fr 44px 64px;font-size:10.5px;line-height:1.6}
  .price-row .amt{font-weight:600;text-align:right}
  .price-row--head{font-weight:600;font-size:9.5px}
  .price-row--head span{text-align:right}
  .price-row--two{grid-template-columns:1fr auto}
  .price-row .note{font-size:8.5px;font-weight:400}
  .billing-note{font-size:9.5px;line-height:1.5;opacity:.92;margin-top:6px}
</style>
</head>
<body>
<main class="brochure">

  <div class="services-band"><span class="light">Our</span><span class="bold">Services</span></div>

  <section class="panel panel--light">
    <div class="panel-body">
      <article class="service service--img-right">
        <div>
          <h2 class="service-title">Chiropractic</h2>
          <p class="service-text">Chiropractic is the assessment, treatment, rehabilitation and prevention of musculoskeletal (bones, muscles, tendons, joints and cartilage) conditions and disorders. Chiropractic care is able to treat these conditions and the effect they have on the nervous system. Learn how we can help you with chiropractic care.</p>
        </div>
        <div class="photo" style="margin-top:16px"><div class="photo-fill tone-skin" role="img" aria-label="Chiropractor adjusting a patient's back"></div></div>
      </article>

      <article class="service service--img-left">
        <div class="photo"><div class="photo-fill tone-linen" role="img" aria-label="Therapist giving a back massage"></div></div>
        <div>
          <h2 class="service-title">Massage Therapy</h2>
          <p class="service-text">Massage Therapy is the assessment and treatment of the soft tissues of the body, specifically, the muscles, connective tissue, tendons, ligaments and joints for the purpose of optimizing health. Learn how we can help you with massage therapy.</p>
        </div>
      </article>

      <article class="service service--img-right">
        <div>
          <h2 class="service-title">Manual Osteopathic Therapy</h2>
          <p class="service-text">Manual Osteopathic Therapy is the assessment and treatment of all of the components that make up the human body. Whether it is organs, musculoskeletal structure, joint issues or an impairment in the circulatory system, a manual osteopath is able to determine the root of your condition and provide an effective treatment to alleviate your symptoms and bring your body back into balance. Learn how we can help you with Manual Osteopathy.</p>
        </div>
        <div class="photo photo--tall" style="margin-top:26px"><div class="photo-fill tone-linen" role="img" aria-label="Osteopath treating a patient's abdomen and knee"></div></div>
      </article>
    </div>
  </section>

  <section class="panel panel--light">
    <div class="panel-body">
      <article class="service service--img-right">
        <div>
          <h2 class="service-title">Acupuncture</h2>
          <p class="service-text">Acupuncture is a Traditional Chinese Medicine technique to improve the body's functions and natural healing ability. It works by stimulating specific anatomical sites, commonly referred to as acupuncture points or acupoints. Learn how we can help you with Acupuncture.</p>
        </div>
        <div class="photo"><div class="photo-fill tone-needle" role="img" aria-label="Acupuncture needles placed in skin"></div></div>
      </article>

      <article class="service service--img-left">
        <div class="photo" style="margin-top:8px"><div class="photo-fill tone-laser" role="img" aria-label="Laser therapy device applied to a leg"></div></div>
        <div>
          <h2 class="service-title">Laser Therapy</h2>
          <p class="service-text">Laser Therapy is a non-invasive, painless treatment which uses focused light at specific wavelengths to help reduce and often eliminate pain from injuries and chronic conditions. Learn how we can help you with laser therapy.</p>
        </div>
      </article>

      <article class="service service--img-right">
        <div>
          <h2 class="service-title">Radial Shockwave Therapy</h2>
          <p class="service-text">Shockwave Therapy is the latest innovation in the treatment of chronic soft tissue injuries. A projectile is propelled inside the hand-piece where it generates a mechanical pressure wave that is transferred to the human body. Learn how we can help you with Shockwave Therapy.</p>
        </div>
        <div class="stack">
          <div class="photo photo--short"><div class="photo-fill tone-device-blue" role="img" aria-label="Shockwave hand-piece on a blue surface"></div></div>
          <div class="photo photo--short"><div class="photo-fill tone-device-grey" role="img" aria-label="Shockwave therapy machine"></div></div>
        </div>
      </article>

      <div class="book">Book Online Now</div>
      <div class="site">
        <svg width="14" height="14" viewBox="0 0 14 14" aria-hidden="true" fill="none" stroke="#1769b5" stroke-width="1.3">
          <circle cx="7" cy="7" r="6"/><ellipse cx="7" cy="7" rx="2.6" ry="6"/><path d="M1 7h12M2 3.8h10M2 10.2h10"/>
        </svg>
        <span>www.<strong>QuillbrookHealth</strong>.ca</span>
      </div>
    </div>
  </section>

  <section class="panel panel--prices">
    <h2 class="prices-title"><span class="light">Our </span><span class="bold">Prices</span></h2>

    <div class="price-group">
      <h3>Massage Therapy</h3>
      <div class="price-row price-row--two"><span>30 Minute</span><span class="amt">$50</span></div>
      <div class="price-row price-row--two"><span>45 Minutes</span><span class="amt">$75</span></div>
      <div class="price-row price-row--two"><span>60 Minutes</span><span class="amt">$90</span></div>
      <div class="price-row price-row--two"><span>90 Minutes</span><span class="amt">$130</span></div>
      <div class="price-row price-row--two"><span>Infant Massage Instruction</span><span class="amt">$50</span></div>
      <div class="price-row price-row--two"><span>Hot Stone Addition</span><span class="amt">+$20 <span class="note">to regular treatment price</span></span></div>
    </div>

    <div class="price-group">
      <h3>Chiropractic</h3>
      <div class="price-row price-row--head"><span></span><span>Initial</span><span>Subsequent</span></div>
      <div class="price-row"><span>Pediatrics 0-5 yr old</span><span class="amt">$115</span><span class="amt">$55</span></div>
      <div class="price-row"><span>Student (6+yrs, full time)</span><span class="amt">$115</span><span class="amt">$55</span></div>
      <div class="price-row"><span>Adult</span><span class="amt">$125</span><span class="amt">$65</span></div>
      <div class="price-row"><span>Senior 65+ yrs</span><span class="amt">$115</span><span class="amt">$55</span></div>
      <div class="price-row"><span>Chiropractic and laser treatment<br>Chiropractic and shockwave therapy</span><span></span><span class="amt">$95</span></div>
    </div>

    <div class="price-group">
      <h3>Acupuncture</h3>
      <div class="price-row price-row--two"><span>Initial Assessment and Treatment</span><span class="amt">$120</span></div>
      <div class="price-row price-row--two"><span>Subsequent Treatment</span><span class="amt">$85</span></div>
    </div>

    <div class="price-group">
      <h3>Laser Therapy</h3>
      <div class="price-row price-row--two"><span>Initial Assessment and Treatment</span><span class="amt">$90</span></div>
      <div class="price-row price-row--two"><span>Subsequent Treatment</span><span class="amt">$50</span></div>
    </div>

    <div class="price-group">
      <h3>Manual Osteopathic Therapy</h3>
      <div class="price-row price-row--two"><span>Initial Assessment and Treatment</span><span class="amt">$150</span></div>
      <div class="price-row price-row--two"><span>Subsequent Treatment</span><span class="amt">$120</span></div>
      <p class="billing-note">Unfortunately at this time, insurance companies do not allow an option for direct billing for Manual Osteopathy, except in the case of Evergate Benefits and Harborline Insurance.</p>
    </div>
  </section>

</main>
</body>
</html>
```